Wedding Invitation for a wedding at home - personal, romantic event

Want a wedding invitation that is to be printed onto card.
Size to be 148mm x 210mm
For it to open like a book not tent card
Have a picture of a house that I want to be the front cover.
I've attached 2 pictures. I like the picture without the man but with the grass
For the photo to become a drawing and the colours to be brighter.
If you could use the picture of us and get us in one of the windows.
If you could put the picture of the dog maybe somewhere on the grass.
Love the colour of the sky in the picture of the beach

Words to be on the inside of the card:
Together with our families
You are invited to the Wedding Reception of Polly Faraway and Ned Bramwick
On Saturday 9th of September 2017 at 6pm
At Bramwick's Keep, 41b, Fennow Crescent, Camberley, Surrey, GU19 7QX
Carriages at 1am
RSVP by Friday 27th of July to 07712 958 061

Words on the Back page:
With all that we have, we've been truly blessed.
Your presence and prayers are all that we request.
But if you desire to give nonetheless,
Monetary gift is one we suggest.

If the pages can be white.
Writing in gold
gold border on all pages

Target Market(s)

Wedding guests

Industry/Entity Type

Wedding

Font styles to use
Script

Requirements
Must have
• Romantic feel. Our wedding colours are white, gold and rose gold.
• Designer to be creative and I do not have much inspiration.
Nice to have
• metallic colours
• Maybe have MR & MRS in gold metallic on the front page

```html
<!DOCTYPE html>
<html lang="en">
<head>
<meta charset="utf-8">
<title>Polly &amp; Ned – Wedding Invitation</title>
<link rel="stylesheet" href="https://fonts.googleapis.com/css2?family=Great+Vibes&family=Cormorant+Garamond:wght@400;500&family=Oswald:wght@500&display=swap">
<style>
  :root{
    --backdrop:#2b2b2b;
    --paper:#ffffff;
    --gold:#a8803a;
    --gold-dark:#7d5a1c;
    --gold-light:#e0c158;
    --blush:#e6d2c0;
    --serif:"Cormorant Garamond", Georgia, serif;
    --script:"Great Vibes", cursive;
    --display:"Oswald", "Arial Narrow", sans-serif;
  }
  *{box-sizing:border-box;margin:0;padding:0}
  html,body{width:1113px;height:1200px;overflow:hidden;background:var(--backdrop)}
  .spread{position:absolute;left:173px;width:751px;height:526px;background:var(--paper);display:flex}
  .spread--outer{top:42px}
  .spread--inner{top:625px}
  .page{position:relative;width:50%;height:100%;overflow:hidden}
  .page__frame{position:absolute;inset:6px;border:2.5px solid var(--gold);
    border-image:linear-gradient(135deg,var(--gold-dark),var(--gold-light),var(--gold-dark),var(--gold-light),var(--gold-dark)) 1}
  .gold-text{background:linear-gradient(120deg,var(--gold-dark) 0%,var(--gold-light) 35%,#9c7424 60%,var(--gold-light) 85%,var(--gold-dark) 100%);
    -webkit-background-clip:text;background-clip:text;color:transparent}
  .verse{position:absolute;top:188px;left:0;right:0;text-align:center;font-family:var(--serif);font-size:13.5px;line-height:17px;color:var(--gold)}
  .verse p+p{margin-top:15px}
  .cover__scene{position:absolute;inset:0;
    background:linear-gradient(180deg,#f3c9c0 0%,#f7d8b4 18%,#dcc3c9 33%,#c99585 55%,#b77a62 72%,#c8d2b8 85%,#e8e0d6 100%)}
  .monogram{position:absolute;left:0;right:0;height:170px}
  .monogram__amp{position:absolute;font-family:var(--script);color:var(--blush);opacity:.85;line-height:1}
  .monogram__name{position:absolute;font-family:var(--script);line-height:1}
  .cover .monogram{top:68px}
  .cover .monogram__amp{left:150px;top:30px;font-size:170px;opacity:.7}
  .cover .monogram__first{left:105px;top:0;font-size:82px}
  .cover .monogram__second{left:95px;top:68px;font-size:82px}
  .cover__request{position:absolute;top:440px;left:60px;right:0;text-align:center;font-family:var(--serif);font-size:12.5px;line-height:13.5px;color:#8f6a2a}
  .cover__wedding{position:absolute;top:468px;left:95px;font-family:var(--script);font-size:40px;letter-spacing:9px;color:var(--gold-dark)}
  .portrait .monogram{top:45px}
  .portrait .monogram__amp{left:150px;top:30px;font-size:170px}
  .portrait .monogram__first{left:105px;top:0;font-size:82px}
  .portrait .monogram__second{left:95px;top:70px;font-size:82px}
  .portrait__photo{position:absolute;left:120px;top:248px;width:166px;height:222px;
    background:linear-gradient(160deg,#6f5a4c 0%,#a27d68 40%,#d5b39b 70%,#5b4a42 100%);border:1px solid var(--gold-light)}
  .details{position:absolute;inset:0;text-align:center;color:var(--gold)}
  .details__script{position:absolute;left:0;right:0;font-family:var(--script);font-size:22px;line-height:1}
  .details__names{position:absolute;top:164px;left:0;right:0;font-family:var(--display);font-weight:500;font-size:17px;line-height:21px;letter-spacing:3px;color:#9a7328}
  .details__info{position:absolute;left:0;right:0;font-family:var(--serif);font-size:12.5px;line-height:14px}
</style>
</head>
<body>
  <section class="spread spread--outer">
    <article class="page back">
      <div class="verse">
        <p>With all that we have, we've been truly blessed.<br>Your presence and prayers are all that we request.</p>
        <p>But if you desire to give nonetheless,<br>Monetary gift is one we suggest.</p>
      </div>
      <div class="page__frame"></div>
    </article>
    <article class="page cover">
      <div class="cover__scene" role="img" aria-label="Soft pastel painting of the family home, a red-brick house among tall pines under a peach and pink sunset sky, with a lawn in front"></div>
      <div class="monogram">
        <span class="monogram__amp">&amp;</span>
        <span class="monogram__name monogram__first gold-text">Ned</span>
        <span class="monogram__name monogram__second gold-text">Polly</span>
      </div>
      <p class="cover__request">Request The Pleasure Of Your Company<br>To Celebrate Their</p>
      <p class="cover__wedding">Wedding</p>
      <div class="page__frame"></div>
    </article>
  </section>

  <section class="spread spread--inner">
    <article class="page portrait">
      <div class="monogram">
        <span class="monogram__amp">&amp;</span>
        <span class="monogram__name monogram__first gold-text">Ned</span>
        <span class="monogram__name monogram__second gold-text">Polly</span>
      </div>
      <div class="portrait__photo" role="img" aria-label="Photograph of the couple together"></div>
      <div class="page__frame"></div>
    </article>
    <article class="page invitation">
      <div class="details">
        <p class="details__script gold-text" style="top:66px">Together with our families</p>
        <p class="details__script gold-text" style="top:100px">You are invited to the Wedding</p>
        <p class="details__script gold-text" style="top:130px">Reception of</p>
        <p class="details__names">POLLY FARAWAY<br>&amp;<br>NED BRAMWICK</p>
        <p class="details__info" style="top:256px">On Saturday 9th of September 2017 at 6pm</p>
        <p class="details__info" style="top:283px">At Bramwick's Keep, 41b, Fennow Crescent,<br>Camberley, Surrey, GU19 7QX</p>
        <p class="details__info" style="top:324px">Carriages at 1:am</p>
        <p class="details__info" style="top:467px">RSVP by<br>Friday 27th of July to 07712 958 061</p>
      </div>
      <div class="page__frame"></div>
    </article>
  </section>
</body>
</html>
```